Residential Remodeling Contractor needs updated business card

I need a new design for my business card.
Name of the company is Corvell Construction. I need a card that commands presence, strength, integrity. I have been in business for 28 years. I am a Residential Remodeling Contractor that covers all aspects of a residential remodel and build.

```html
<!DOCTYPE html>
<html lang="en">
<head>
<meta charset="utf-8">
<title>Corvell Construction – Business Card</title>
<link rel="stylesheet" href="https://fonts.googleapis.com/css2?family=Cinzel:wght@600&family=EB+Garamond:ital,wght@0,400;0,600;1,400&display=swap">
<style>
  :root {
    --brand-blue: #1f3c7e;
    --paper: #ffffff;
    --ink: #4a4a4a;
    --backdrop: #e6e7ea;
  }
  * { box-sizing: border-box; margin: 0; padding: 0; }
  html, body { width: 1200px; height: 833px; overflow: hidden; }
  body {
    background: var(--backdrop);
    display: flex;
    flex-direction: column;
    align-items: center;
    justify-content: center;
    gap: 44px;
    font-family: "EB Garamond", Georgia, serif;
  }
  .card {
    width: 600px;
    height: 343px;
    border-radius: 22px;
    position: relative;
    overflow: hidden;
    box-shadow: 0 6px 18px rgba(0,0,0,.12);
  }
  .card--front { background: var(--brand-blue); display: flex; align-items: center; justify-content: center; }
  .card--back { background: var(--paper); }

  .wordmark { display: flex; align-items: center; gap: 18px; font-family: "Cinzel", "Times New Roman", serif; font-weight: 600; }
  .wordmark__square { width: 22px; height: 22px; }
  .wordmark__text { line-height: 1; }
  .wordmark__line1 { display: block; letter-spacing: .02em; }
  .wordmark__line2 { display: block; letter-spacing: .04em; }

  .card--front .wordmark { color: var(--paper); }
  .card--front .wordmark__square { background: var(--paper); }
  .card--front .wordmark__line1 { font-size: 54px; }
  .card--front .wordmark__line2 { font-size: 34px; margin-top: 8px; }

  .card--back .wordmark { position: absolute; left: 46px; top: 52px; color: var(--brand-blue); gap: 12px; }
  .card--back .wordmark__square { background: var(--brand-blue); width: 16px; height: 16px; }
  .card--back .wordmark__line1 { font-size: 34px; }
  .card--back .wordmark__line2 { font-size: 21px; margin-top: 5px; }

  .contact { position: absolute; left: 50px; top: 150px; list-style: none; color: var(--ink); font-size: 16.5px; line-height: 1.3; }
  .contact li { display: flex; align-items: flex-start; gap: 12px; }
  .contact svg { width: 13px; height: 13px; margin-top: 4px; fill: var(--brand-blue); flex-shrink: 0; }

  .person { position: absolute; right: 46px; top: 150px; text-align: right; }
  .person__name { font-weight: 600; color: var(--brand-blue); font-size: 30px; letter-spacing: .03em; text-transform: uppercase; line-height: 1; }
  .person__title { font-style: italic; color: var(--ink); font-size: 18px; margin-top: 4px; }

  .edge-tab { position: absolute; right: 0; top: 70px; width: 10px; height: 70px; background: var(--brand-blue); }
</style>
</head>
<body>

  <section class="card card--front" aria-label="Card front">
    <div class="wordmark">
      <span class="wordmark__square" aria-hidden="true"></span>
      <span class="wordmark__text">
        <span class="wordmark__line1">Corvell</span>
        <span class="wordmark__line2">Construction</span>
      </span>
    </div>
  </section>

  <section class="card card--back" aria-label="Card back">
    <div class="wordmark">
      <span class="wordmark__square" aria-hidden="true"></span>
      <span class="wordmark__text">
        <span class="wordmark__line1">Corvell</span>
        <span class="wordmark__line2">Construction</span>
      </span>
    </div>

    <ul class="contact">
      <li>
        <svg viewBox="0 0 16 16" aria-hidden="true"><path d="M8 0a5.5 5.5 0 0 0-5.5 5.5C2.5 10 8 16 8 16s5.5-6 5.5-10.5A5.5 5.5 0 0 0 8 0zm0 8a2.5 2.5 0 1 1 0-5 2.5 2.5 0 0 1 0 5z"/></svg>
        <span>4870 Birchwood Lane<br>Milford, CT 06460</span>
      </li>
      <li>
        <svg viewBox="0 0 16 16" aria-hidden="true"><path d="M3.6 1l2.5 3-1.5 1.8a9 9 0 0 0 5.6 5.6L12 9.9l3 2.5-1.4 2.6C7.5 15.5.5 8.5 1 2.4z"/></svg>
        <span>(203) 555-0147</span>
      </li>
      <li>
        <svg viewBox="0 0 16 16" aria-hidden="true"><path d="M4.5 0h7A1.5 1.5 0 0 1 13 1.5v13a1.5 1.5 0 0 1-1.5 1.5h-7A1.5 1.5 0 0 1 3 14.5v-13A1.5 1.5 0 0 1 4.5 0zM5 2v10h6V2zm3 11a1 1 0 1 0 0 2 1 1 0 0 0 0-2z"/></svg>
        <span>(203) 555-0182</span>
      </li>
      <li>
        <svg viewBox="0 0 16 16" aria-hidden="true"><path d="M4 1h8v4H4zM1 6h14v7h-3v2H4v-2H1zm4 4v4h6v-4z"/></svg>
        <span>(203) 555-0193</span>
      </li>
      <li>
        <svg viewBox="0 0 16 16" aria-hidden="true"><path d="M0 3h16v1L8 9 0 4zm0 3l8 5 8-5v7H0z"/></svg>
        <span>info@corvellbuild.com</span>
      </li>
      <li>
        <svg viewBox="0 0 16 16" aria-hidden="true"><path d="M8 0a8 8 0 1 0 0 16A8 8 0 0 0 8 0zm0 1.5c1 0 2 2.2 2.3 5H5.7C6 3.7 7 1.5 8 1.5zm-2.3 6.5h4.6C10 10.8 9 14.5 8 14.5S6 10.8 5.7 8z"/></svg>
        <span>corvellbuild.com</span>
      </li>
    </ul>

    <div class="person">
      <p class="person__name">Daniel Harlow</p>
      <p class="person__title">Founder &amp; CEO</p>
    </div>

    <span class="edge-tab" aria-hidden="true"></span>
  </section>

</body>
</html>
```